Professional
Miriam T. Hollisby, Esq.
Attorney at Law
Hollisby & Dunmore, LLC
4127 Fernhaven Court
Atlanta, Georgia 30305
mhollisby@hd-counsel.net
www.hd-counsel.net
I may want to include a photo. I have uploaded a photo. I'd like to see if it looks appropriate, if not, we'll go without a photo. Please use the logo that is uploaded
Please use the logo that is uploaded in some way. Possibly the corresponding black background with whitel letters for the back.
Photo to possibly be included on busines cards

```html
<!DOCTYPE html>
<html lang="en">
<head>
<meta charset="utf-8">
<title>Hollisby &amp; Dunmore, LLC — Business Cards</title>
<link rel="stylesheet" href="https://fonts.googleapis.com/css2?family=Cormorant+SC:wght@500;600&family=Open+Sans:wght@400;600&display=swap">
<style>
  :root {
    --backdrop: #3a3a3a;
    --paper-grey-top: #f1f0ef;
    --paper-grey-bottom: #d9d8d6;
    --legal-red: #b0171c;
    --legal-red-dark: #7e0d10;
    --legal-red-light: #c8262b;
    --ink-dark: #2b2b2b;
    --ink-white: #ffffff;
    --card-black: #0c0c0c;
    --card-white: #ffffff;
    --divider-dark: #3a3a3a;
  }
  * { box-sizing: border-box; margin: 0; padding: 0; }
  html, body { width: 1200px; height: 852px; overflow: hidden; }
  body {
    background: var(--backdrop);
    position: relative;
    font-family: "Open Sans", Arial, sans-serif;
  }
  .card {
    position: absolute;
    width: 490px;
    height: 280px;
    box-shadow: 0 8px 22px rgba(0,0,0,0.45);
    overflow: hidden;
  }
  .card--front { left: 355px; top: 80px; }
  .card--back-light { left: 90px; top: 470px; background: var(--card-white); }
  .card--back-dark { left: 620px; top: 470px; background: var(--card-black); }

  .front__upper {
    position: absolute; left: 0; top: 0; width: 100%; height: 150px;
    background: linear-gradient(var(--paper-grey-top), var(--paper-grey-bottom));
    border-bottom: 4px solid var(--divider-dark);
  }
  .front__lower {
    position: absolute; left: 0; top: 154px; width: 100%; height: 126px;
    background: radial-gradient(ellipse at 50% 0%, var(--legal-red-light), var(--legal-red) 45%, var(--legal-red-dark));
    color: var(--ink-white);
    display: flex;
    padding: 22px 0 0 42px;
  }

  .brand {
    position: absolute;
    display: flex; align-items: center; gap: 12px;
  }
  .brand__mark {
    width: 46px; height: 46px; border-radius: 50%;
    background: var(--legal-red);
    flex: none;
  }
  .brand__name {
    font-family: "Cormorant SC", Georgia, serif;
    font-weight: 600;
    font-size: 27px;
    letter-spacing: 0.5px;
    color: var(--ink-dark);
    white-space: nowrap;
  }
  .front__upper .brand { left: 40px; top: 52px; }
  .card--back-light .brand { left: 50%; top: 110px; transform: translateX(-50%); }
  .card--back-dark .brand { left: 50%; top: 110px; transform: translateX(-50%); }
  .card--back-dark .brand__mark { background: var(--ink-white); }
  .card--back-dark .brand__name { color: var(--ink-white); }

  .contact-person {
    font-family: "Cormorant SC", Georgia, serif;
    font-weight: 500;
    font-size: 15px;
    line-height: 1.25;
    width: 210px;
  }
  .contact-person__name { font-size: 17px; font-weight: 600; }
  .contact-person__title { padding-left: 38px; margin-bottom: 8px; }
  .contact-person__address { padding-left: 38px; }

  .contact-lines {
    border-left: 1px solid rgba(255,255,255,0.55);
    padding-left: 14px;
    font-size: 11px;
    line-height: 1.6;
    letter-spacing: 0.3px;
  }

  .back__url {
    position: absolute; left: 0; right: 0; bottom: 24px;
    text-align: center;
    font-size: 11px;
    color: var(--legal-red);
  }
  .card--back-dark .back__url { color: var(--legal-red-light); }
</style>
</head>
<body>

  <section class="card card--front" aria-label="Business card front">
    <div class="front__upper">
      <div class="brand">
        <span class="brand__mark"></span>
        <span class="brand__name">Hollisby &amp; Dunmore, LLC</span>
      </div>
    </div>
    <div class="front__lower">
      <div class="contact-person">
        <p class="contact-person__name">Miriam T. Hollisby, Esq.</p>
        <p class="contact-person__title">Attorney at Law</p>
        <p class="contact-person__address">4127 Fernhaven Court<br>Atlanta, Georgia 30305</p>
      </div>
      <div class="contact-lines">
        <p>P : 404-555-0172</p>
        <p>F : 404-555-0179</p>
        <p>mhollisby@hd-counsel.net</p>
        <p>www.hd-counsel.net</p>
      </div>
    </div>
  </section>

  <section class="card card--back-light" aria-label="Business card back, light">
    <div class="brand">
      <span class="brand__mark"></span>
      <span class="brand__name">Hollisby &amp; Dunmore, LLC</span>
    </div>
    <p class="back__url">www.hd-counsel.net</p>
  </section>

  <section class="card card--back-dark" aria-label="Business card back, dark">
    <div class="brand">
      <span class="brand__mark"></span>
      <span class="brand__name">Hollisby &amp; Dunmore, LLC</span>
    </div>
    <p class="back__url">www.hd-counsel.net</p>
  </section>

</body>
</html>
```